Awesome Web Design Project

must have a link to mingleton of the homepage preferably a scrolling view of our mingleton page!

We are an exciting new electrical company with a strong focus on energy efficiency and offering the latest technologies.

The design should allow easy navigation, there shouldn't be too many menus, It should look clean and sleek, Colours to consider could be green, silver/chrome, black,

The site should convey technology, efficiency and simplicity

Must be viewable on all devices, pc's, tablets, phones ie Responsive
Updates

Logo and some pics uploaded!

Industry/Entity Type

Electrical

Requirements
Must have
• must include the following pages,
about us
our services
gallery
contact us
Connect with us
Nice to have
• Would be great if the website design used a user friendly cms,
Should not have
• too many links, menus, clutter it should be clean and easy to navigate

```html
<!DOCTYPE html>
<html lang="en">
<head>
<meta charset="utf-8">
<title>Wren Electrical</title>
<link href="https://fonts.googleapis.com/css2?family=Open+Sans:wght@400;600;700&family=Questrial&display=swap" rel="stylesheet">
<style>
:root{
  --lime:#b4c832;
  --lime-dark:#98ab22;
  --ink:#3a3a3a;
  --muted:#6d6d6d;
  --paper:#ffffff;
  --mist:#e9eaea;
  --line:#d4d6d6;
  --band:#3f5b5d;
  --night:#2f3233;
  --night-text:#b9bcbc;
  --copper:#c8753a;
}
*{box-sizing:border-box;margin:0;padding:0}
html,body{width:872px;height:1200px;overflow:hidden;background:var(--paper)}
body{font-family:"Open Sans",Arial,sans-serif;color:var(--ink);font-size:9px;line-height:1.45}
.page{position:relative;width:872px;height:1200px}

.utility{position:absolute;top:0;right:14px;display:flex;gap:3px}
.utility span{background:var(--night);color:#ddd;font-size:7.5px;padding:2px 12px}

.site-header{position:absolute;top:0;left:0;width:872px;height:85px}
.brand{position:absolute;left:20px;top:22px;display:flex;align-items:center;gap:8px}
.brand-mark{width:26px;height:26px;background:var(--lime)}
.brand-name{font-family:"Questrial",sans-serif;font-size:22px;color:var(--ink);letter-spacing:1px}
.main-nav{position:absolute;right:14px;top:38px;display:flex;gap:4px}
.main-nav a{background:var(--lime);color:#fff;text-decoration:none;font-size:9px;padding:5px 13px}

.hero{position:absolute;top:85px;left:0;width:872px;height:272px;
  background:radial-gradient(ellipse at 45% 55%,#e9a66a 0%,var(--copper) 18%,#5a3a2a 42%,#1e1e22 70%),#222}

.welcome{position:absolute;top:392px;left:60px;width:752px;text-align:center}
.welcome h1{font-family:"Questrial",sans-serif;font-weight:400;font-size:25px;letter-spacing:1px;color:var(--ink);margin-bottom:12px}
.welcome p{font-size:9px;color:var(--muted);text-align:left}
.welcome p b{color:var(--ink)}
.btn{display:inline-block;background:var(--lime);color:#fff;font-size:9.5px;padding:8px 22px;text-decoration:none;border:1px solid var(--lime-dark)}
.welcome .btn{margin-top:42px}

.features{position:absolute;top:615px;left:0;width:872px;height:320px;background:var(--mist)}
.col{position:absolute;top:22px}
.col h2{font-family:"Questrial",sans-serif;font-weight:400;font-size:13px;color:var(--ink);padding-bottom:4px;border-bottom:1px solid var(--line);margin-bottom:8px}
.col p{font-size:8px;color:var(--muted);margin-bottom:8px}
.col .more{font-size:8px;color:var(--ink);font-weight:600}
.col-about{left:48px;width:210px}
.col-projects{left:338px;width:220px}
.col-social{left:575px;width:250px}
.project-photo{width:220px;height:100px;background:linear-gradient(135deg,#8a8f95,#c9c7c0 55%,#6f6a62);margin-bottom:8px}
.widget{background:#fff;border:1px solid var(--line);padding:8px;height:176px}
.widget-head{display:flex;gap:8px;align-items:center;border-bottom:1px solid var(--line);padding-bottom:6px;margin-bottom:6px}
.widget-head .sq{width:28px;height:28px;background:var(--lime)}
.widget-head b{font-size:9px}
.widget-head small{display:block;font-size:7px;color:var(--muted)}
.widget h3{font-size:8px;margin-bottom:4px}
.post{display:flex;gap:6px;margin-bottom:6px;font-size:7px;color:var(--muted)}
.post i{flex:none;width:20px;height:20px;background:var(--lime)}

.cta-services{position:absolute;top:936px;left:0;width:872px;text-align:center}

.call-band{position:absolute;top:970px;left:0;width:872px;height:55px;background:var(--band);color:#fff;
  font-family:"Questrial",sans-serif;font-size:17px;display:flex;align-items:center;justify-content:center;gap:8px;letter-spacing:.5px}
.call-band strong{font-family:"Open Sans",sans-serif;font-weight:700}

.site-footer{position:absolute;top:1025px;left:0;width:872px;height:175px;background:var(--night);color:var(--night-text)}
.fcol{position:absolute;top:20px}
.fcol h4{font-family:"Questrial",sans-serif;font-weight:400;font-size:10px;color:#fff;letter-spacing:.5px;margin-bottom:10px}
.fcol li{list-style:none;font-size:7.5px;margin-bottom:2px}
.fcol p{font-size:7.5px;margin-bottom:6px}
.f-links{left:34px;width:120px}
.f-news{left:196px;width:200px}
.f-news p{border-bottom:1px solid #45494a;padding-bottom:5px}
.f-letter{left:465px;width:170px}
.f-letter label{display:block;font-size:7.5px;margin-bottom:2px}
.f-letter .field{height:14px;background:#fff;margin-bottom:5px}
.f-letter .send{display:inline-block;background:#fff;color:var(--ink);font-size:7.5px;padding:2px 10px}
.f-contact{left:660px;width:180px}
.socials{display:flex;gap:5px;margin-top:6px}
.socials span{width:16px;height:16px;border-radius:50%;background:var(--lime)}
.legal{position:absolute;bottom:6px;left:34px;font-size:6.5px;color:#888}
</style>
</head>
<body>
<div class="page">

  <header class="site-header">
    <div class="utility"><span>mingleton</span><span>Contact us</span></div>
    <div class="brand"><span class="brand-mark"></span><span class="brand-name">WREN ELECTRICAL</span></div>
    <nav class="main-nav">
      <a href="#">Home</a><a href="#">About us</a><a href="#">Our services</a><a href="#">Gallery</a><a href="#">Contact us</a>
    </nav>
  </header>

  <div class="hero" role="img" aria-label="Close-up photograph of stripped electrical cables with copper strands"></div>

  <section class="welcome">
    <h1>WELCOME TO WREN ELECTRICAL</h1>
    <p>We are a new electrical company with a firm focus on energy efficiency and the latest technologies. From a single socket to a complete rewire, our qualified team plans every job around lower running costs, safer wiring and tidy finishes. We install smart lighting, efficient heating controls, solar ready consumer units and car charging points for homes and businesses alike, and we keep you informed at every stage so there are no surprises when the work is done. <b>...read more</b></p>
    <a class="btn" href="#">See our clients and past projects</a>
  </section>

  <section class="features">
    <div class="col col-about">
      <h2>About us</h2>
      <p>Wren Electrical was founded by engineers who believe good wiring should cost less to run. We combine careful workmanship with modern, efficient products and clear advice.</p>
      <p>Every installation is tested and certified, and our team stays trained on new technology so your home or business is ready for what comes next.</p>
      <p>We work across the region and offer free, no obligation estimates.</p>
      <span class="more">...read more</span>
    </div>
    <div class="col col-projects">
      <h2>Completed Projects</h2>
      <div class="project-photo" role="img" aria-label="Photograph of a finished interior electrical installation"></div>
      <p>A full rewire with low energy lighting and smart controls for a family home, finished on time and on budget.</p>
      <span class="more">...read more</span>
    </div>
    <div class="col col-social">
      <h2>Join our mingleton</h2>
      <div class="widget">
        <div class="widget-head"><span class="sq"></span><div><b>Wren Electrical</b><small>128 people follow this page</small></div></div>
        <h3>Recent Activity</h3>
        <div class="post"><i></i><span>New smart lighting job completed this week in the town centre.</span></div>
        <div class="post"><i></i><span>Tips for cutting your standby power use at home this winter.</span></div>
        <div class="post"><i></i><span>We now install home car charging points, ask us for a quote.</span></div>
      </div>
    </div>
  </section>

  <div class="cta-services"><a class="btn" href="#">View all our services</a></div>

  <div class="call-band">GIVE WREN ELECTRICAL A CALL RIGHT NOW AND GET YOUR FREE ESTIMATE! <strong>0800-555-0199</strong></div>

  <footer class="site-footer">
    <div class="fcol f-links">
      <h4>USEFUL LINKS</h4>
      <ul><li>Home</li><li>About us</li><li>Our services</li><li>Gallery</li><li>Contact us</li><li>Connect with us</li></ul>
    </div>
    <div class="fcol f-news">
      <h4>LATEST NEWS &amp; EVENTS</h4>
      <p>New efficient lighting range now available for home and office installs.</p>
      <p>Our team completes advanced training in solar ready systems.</p>
      <p>Open day at our workshop next month, everyone is welcome.</p>
    </div>
    <div class="fcol f-letter">
      <h4>NEWSLETTER</h4>
      <label>Name</label><div class="field"></div>
      <label>Email</label><div class="field"></div>
      <span class="send">Sign up</span>
    </div>
    <div class="fcol f-contact">
      <h4>QUICK CONTACTS</h4>
      <p>Tel: 0800-555-0199<br>12 Meadow Lane, Northfield<br>hello@wrenelectrical.test</p>
      <div class="socials"><span></span><span></span><span></span></div>
    </div>
    <div class="legal">© Wren Electrical. All rights reserved.</div>
  </footer>

</div>
</body>
</html>
```